Plakat-Design für Eis
Zielgruppe
Wir sind ein kleiner regionaler Eisproduzent, betreiben ein Eiscafe mit eigener Eisproduktion. Wir füllen unsere Produkte in Plastebecher ab und vermarkten sie im Einzelhandel, an Tankstellen und zu Festen aller Art. Um diese Becher noch besser zu vermarkten, möchten wir von Zeit zu Zeit mit einem neuen Plakatdesign auf uns aufmerksam machen und wünschen uns daß Sie uns dabei helfen können.
Aufgabenstellung
Bei unseren neuen Werbeplakat wünschen wir uns, daß der Kunde schon beim anschauen das Verlangen nach unserem Eisprodukt verspürt. Der Becher sollte unverkennbar im Mittelpunkt der Aufmerksamkeit stehen. Da wir mit dem Bezug auf Regionalität werben,können wir uns vorstellen, eventl. einen typisch landschaftlichen Hindergrund mit einzubauen(Thüringen). Dies ist aber nicht zwingend unsere Vorstellung, sind aber für gut gemachte Ideen offen. Die Plakate werden später in verschiedenen Größen gebraucht (A3,A2,A1). In der Anlage haben wir zur Orientierung unser altes Plakat reingestellt, freuen uns aber über neue Ideen. Weiterhin sind Dateien vom Logo und diversen Becherbildern die bei der Neugestaltung verwendet werden dürfen.

```html
<!DOCTYPE html>
<html lang="de">
<head>
<meta charset="utf-8">
<title>Plakatentwürfe Softeis im Becher</title>
<link href="https://fonts.googleapis.com/css2?family=Kaushan+Script&family=Raleway:wght@300;500&family=Fira+Sans:wght@700&display=swap" rel="stylesheet">
<style>
  :root {
    --sheet: #ffffff;
    --frame: #c9c9c9;
    --pink: #dcb3d7;
    --lime: #a3bb29;
    --olive: #76901f;
    --sky: #b5c6e3;
    --grey: #6d6d6d;
    --ink: #111111;
  }
  * { box-sizing: border-box; margin: 0; padding: 0; }
  html, body { width: 1200px; height: 792px; overflow: hidden; background: var(--sheet); }
  .sheet { position: relative; width: 1200px; height: 792px; }

  .poster {
    position: absolute; top: 85px; width: 418px; height: 592px;
    border: 2px solid var(--frame); background: var(--sheet); overflow: hidden;
  }
  .poster--one { left: 96px; }
  .poster--two { left: 659px; }

  .swirl {
    position: absolute; left: 30px; top: 8px; width: 390px; height: 460px;
    border-radius: 48% 40% 30% 30%;
    background: radial-gradient(ellipse at 60% 45%, rgba(163,187,41,.35) 0%, rgba(181,198,227,.35) 55%, rgba(255,255,255,0) 75%);
  }

  .brand { position: absolute; left: 12px; top: 52px; display: flex; align-items: center; gap: 5px; }
  .brand__dot { width: 12px; height: 12px; border-radius: 50%; background: var(--sky); }
  .brand__name { font-family: "Raleway", sans-serif; font-weight: 500; font-size: 17px; color: var(--lime); }

  .headline {
    position: absolute; left: 20px; top: 130px;
    font-family: "Kaushan Script", cursive; color: var(--pink);
    text-shadow: -3px 3px 0 var(--grey), 2px 2px 0 var(--lime);
    line-height: 1;
  }
  .headline__line1 { display: block; font-size: 84px; }
  .headline__line2 { display: block; font-size: 80px; margin-top: 8px; text-transform: uppercase; letter-spacing: -2px; }

  .tagline {
    position: absolute; left: 26px; top: 330px;
    font-family: "Kaushan Script", cursive; font-size: 30px; color: var(--grey);
  }

  .claim {
    position: absolute; left: 12px; top: 485px;
    font-family: "Raleway", sans-serif; font-weight: 300; font-size: 14px; line-height: 17px;
  }
  .claim__pink { color: var(--pink); }
  .claim__blue { color: var(--sky); }
  .claim__lime { color: var(--lime); }
  .claim__grey { color: var(--grey); }

  .cup { position: absolute; border-radius: 50%; border: 6px solid #eeeeee; }
  .poster--one .cup--a { left: 272px; top: 378px; width: 150px; height: 150px; background: radial-gradient(circle, #c5cbbd, #8e9888); }
  .poster--one .cup--b { left: 170px; top: 415px; width: 160px; height: 160px; background: radial-gradient(circle, #d3c3cf, #7d6476); }
  .poster--one .cup--c { left: 278px; top: 465px; width: 150px; height: 150px; background: radial-gradient(circle, #d6d8dc, #868b94); }
  .poster--two .cup--a { left: 325px; top: 415px; width: 140px; height: 150px; background: radial-gradient(circle, #d9ecd0, #4db7e0); }
  .poster--two .cup--c { left: 250px; top: 480px; width: 150px; height: 150px; background: radial-gradient(circle, #d9ecd0, #6dc3e4); }
  .poster--two .cup--b { left: 170px; top: 403px; width: 175px; height: 175px; background: radial-gradient(circle, #e4f0d0 20%, #47b3df 75%); }

  .caption {
    position: absolute; top: 715px;
    font-family: "Fira Sans", sans-serif; font-weight: 700; font-size: 17px; color: var(--ink);
  }
  .caption--one { left: 96px; }
  .caption--two { left: 662px; }
</style>
</head>
<body>
<main class="sheet">
  <section class="poster poster--one">
    <div class="swirl" role="img" aria-label="Große grün-blaue Softeis-Swirl-Illustration"></div>
    <div class="brand"><span class="brand__dot"></span><span class="brand__name">wiesenkamm</span></div>
    <h1 class="headline"><span class="headline__line1">eis, eis</span><span class="headline__line2">Becher!</span></h1>
    <p class="tagline">mmmmh … so fein!</p>
    <div class="cup cup--a" role="img" aria-label="Softeisbecher, entsättigt grün"></div>
    <div class="cup cup--b" role="img" aria-label="Softeisbecher Heidelbeer-Vanille, entsättigt mauve"></div>
    <div class="cup cup--c" role="img" aria-label="Softeisbecher, entsättigt grau"></div>
    <p class="claim">
      <span class="claim__pink">Da Softeis im Becher.</span><br>
      <span class="claim__blue">NATÜRLICH LECKER</span><br>
      <span class="claim__lime">aus Thüringen.</span><br>
      <span class="claim__grey">Probieren Sie die vielen<br>Sorten von Wiesenkamm.</span>
    </p>
  </section>

  <section class="poster poster--two">
    <div class="swirl" role="img" aria-label="Große grün-blaue Softeis-Swirl-Illustration"></div>
    <div class="brand"><span class="brand__dot"></span><span class="brand__name">wiesenkamm</span></div>
    <h1 class="headline"><span class="headline__line1">eis, eis</span><span class="headline__line2">Becher!</span></h1>
    <p class="tagline">mmmmh … so fein!</p>
    <div class="cup cup--a" role="img" aria-label="Softeisbecher, blau-grün"></div>
    <div class="cup cup--c" role="img" aria-label="Softeisbecher, blau-grün"></div>
    <div class="cup cup--b" role="img" aria-label="Softeisbecher Heidelbeer-Vanille, blau-grün mit rot-gelbem Band"></div>
    <p class="claim">
      <span class="claim__pink">Da Softeis im Becher.</span><br>
      <span class="claim__blue">NATÜRLICH LECKER</span><br>
      <span class="claim__lime">aus Thüringen.</span><br>
      <span class="claim__grey">Probieren Sie die vielen<br>Sorten von Wiesenkamm.</span>
    </p>
  </section>

  <p class="caption caption--one">Entwurf 1</p>
  <p class="caption caption--two">Entwurf 2</p>
</main>
</body>
</html>
```